Endocrinologist needs new stationery

I have a logo from MarkForge and now need stationery with the new logo.

Address: Suite 4, 282 Falcon Street, Richmond, VIC 3121
Phone: 03 9417 2253
Fax: 03 9417 2255
Website: www.drmaylacorwen.com.au
Email: admin@drmaylacorwen.com.au

```html
<!DOCTYPE html>
<html lang="en">
<head>
<meta charset="utf-8">
<title>Dr Mayla Corwen Endocrinology – Letterhead</title>
<link href="https://fonts.googleapis.com/css2?family=Crimson+Text:wght@400;600&display=swap" rel="stylesheet">
<style>
  :root {
    --backdrop: #e3e3e3;
    --paper: #ffffff;
    --brand-blue: #2f6b9a;
    --brand-mauve: #7a4a5e;
    --ink: #1e1e1e;
    --white: #ffffff;
  }
  * { box-sizing: border-box; margin: 0; padding: 0; }
  html, body {
    width: 977px; height: 1200px; overflow: hidden;
    background: var(--backdrop);
    font-family: "Crimson Text", Georgia, serif;
  }
  .letterhead {
    position: absolute; left: 122px; top: 84px;
    width: 730px; height: 1032px;
    background: var(--paper);
  }
  .brand {
    position: absolute; left: 49px; top: 80px;
    font-size: 38px; font-weight: 400; line-height: 1;
    color: var(--brand-blue);
    letter-spacing: 0.5px;
  }
  .brand-rule {
    position: absolute; left: 49px; top: 125px;
    width: 296px; height: 1px; background: var(--brand-mauve);
  }
  .contact-divider {
    position: absolute; left: 459px; top: 48px;
    width: 2px; height: 98px; background: var(--brand-mauve);
  }
  .contact {
    position: absolute; left: 475px; top: 46px;
    list-style: none; color: var(--ink);
    font-size: 13px; line-height: 16px;
  }
  .contact li { position: relative; padding-left: 22px; }
  .contact li + li { margin-top: 2px; }
  .contact .address-item { margin-bottom: 3px; }
  .contact svg {
    position: absolute; left: 0; top: 3px; width: 10px; height: 10px;
    fill: var(--brand-blue);
  }
  .contact .practice-name { font-weight: 600; }
  .contact .phone { font-size: 14px; letter-spacing: 0.3px; }
  .footer-rule {
    position: absolute; left: 0; width: 100%; height: 2px;
    background: var(--brand-mauve);
  }
  .footer-rule.upper { top: 993px; }
  .footer-band {
    position: absolute; left: 0; top: 999px; width: 100%; height: 33px;
    background: var(--brand-blue); color: var(--white);
    display: flex; align-items: center; justify-content: center;
    font-size: 14px; font-weight: 600; letter-spacing: 2.2px;
  }
</style>
</head>
<body>
<main class="letterhead">
  <div class="brand">Dr Mayla Corwen</div>
  <div class="brand-rule"></div>

  <div class="contact-divider"></div>
  <ul class="contact">
    <li class="address-item">
      <svg viewBox="0 0 10 10"><path d="M5 0a3.6 3.6 0 0 0-3.6 3.6C1.4 6.3 5 10 5 10s3.6-3.7 3.6-6.4A3.6 3.6 0 0 0 5 0zm0 5a1.4 1.4 0 1 1 0-2.8A1.4 1.4 0 0 1 5 5z"/></svg>
      <span class="practice-name">DrMaylaCorwen Endocrinology</span><br>
      Suite 4, 282 Falcon Street<br>
      Richmond, VIC 3121
    </li>
    <li class="phone">
      <svg viewBox="0 0 10 10"><path d="M2 0.5l1.6 2.2-1 1a6 6 0 0 0 3.7 3.7l1-1L9.5 8 8.4 9.5C4 9.5 0.5 6 0.5 1.6z"/></svg>
      03 9417 2253
    </li>
    <li class="phone">
      <svg viewBox="0 0 10 10"><path d="M2.5 0.5h5v2.5h-5zM1 3.5h8a1 1 0 0 1 1 1V7H8v2.5H2V7H0V4.5a1 1 0 0 1 1-1zm2 3.5v1.6h4V7z"/></svg>
      03 9417 2255
    </li>
    <li>
      <svg viewBox="0 0 10 10"><path d="M0.5 2h9v0.8L5 5.6 0.5 2.8zM0.5 3.9 5 6.7l4.5-2.8V8h-9z"/></svg>
      admin@drmaylacorwen.com.au
    </li>
  </ul>

  <div class="footer-rule upper"></div>
  <footer class="footer-band">WWW.DRMAYLACORWEN.COM.AU</footer>
</main>
</body>
</html>
```